French for French

Cover for the book "The Plume Vagabonde" ("How to write in French"). The book seeks to teach English to English: words, grammar, syntax. The lessons are pleasant, the style is very classical.

Target Market(s)

Middle class interested in improving her language.

Industry/Entity Type

Publishing Company

Colors

Designer to choose colors to be used in the design.

Requirements
Must have
• Author: "Bernard Morlaix" Title: "The Lively Pen" Publisher: "Quillon Editions" Size: 14 x 20,5 cm

```html
<!DOCTYPE html>
<html lang="en">
<head>
<meta charset="utf-8">
<title>The Lively Pen — Bernard Morlaix</title>
<link rel="stylesheet" href="https://fonts.googleapis.com/css2?family=Roboto+Condensed:wght@400;500&family=Caveat+Brush&display=swap">
<style>
  :root {
    --paper: #ffffff;
    --ink: #111111;
    --accent-red: #ee1c0f;
    --arc-shade: #8a8c8e;
    --arc-light: #e6e7e8;
    --burst-warm: #f7c94a;
    --burst-cool: #7fd0ef;
    --burst-pink: #f4a0c8;
    --burst-green: #9be26b;
  }
  * { box-sizing: border-box; margin: 0; padding: 0; }
  html, body { width: 820px; height: 1200px; overflow: hidden; background: var(--paper); }
  .cover {
    position: relative;
    width: 820px;
    height: 1200px;
    background: var(--paper);
    font-family: "Roboto Condensed", "Arial Narrow", sans-serif;
    color: var(--ink);
  }
  .cover__author {
    position: absolute;
    top: 58px;
    left: 0;
    width: 100%;
    text-align: center;
    font-size: 50px;
    font-weight: 500;
    letter-spacing: 1px;
    line-height: 1;
  }
  .cover__illustration {
    position: absolute;
    top: 135px;
    left: 20px;
    width: 780px;
    height: 460px;
    border-radius: 48% 48% 6% 6% / 60% 60% 4% 4%;
    background:
      radial-gradient(circle at 22% 30%, var(--accent-red) 0 4%, transparent 14%),
      radial-gradient(circle at 70% 22%, var(--burst-warm) 0 5%, transparent 20%),
      radial-gradient(circle at 15% 70%, var(--burst-cool) 0 6%, transparent 22%),
      radial-gradient(circle at 55% 50%, var(--accent-red) 0 3%, transparent 16%),
      radial-gradient(circle at 80% 55%, var(--burst-pink) 0 4%, transparent 20%),
      radial-gradient(circle at 40% 85%, var(--burst-green) 0 6%, transparent 24%),
      radial-gradient(ellipse at 50% 70%, #fbefd9 0 40%, var(--paper) 75%);
  }
  .cover__arc {
    position: absolute;
    top: 575px;
    left: 0;
    width: 820px;
    height: 80px;
  }
  .cover__title {
    position: absolute;
    top: 640px;
    left: 0;
    width: 100%;
    text-align: center;
    font-family: "Caveat Brush", cursive;
    line-height: 1;
  }
  .cover__title-main {
    display: block;
    font-size: 150px;
    color: var(--ink);
  }
  .cover__title-echo {
    display: inline-block;
    margin-top: 14px;
    font-size: 160px;
    color: var(--accent-red);
    padding: 0 12px 0;
    border-bottom: 12px solid var(--accent-red);
    line-height: 0.9;
  }
  .cover__publisher {
    position: absolute;
    top: 1070px;
    left: 0;
    width: 100%;
    text-align: center;
    font-size: 40px;
    font-weight: 400;
    line-height: 1;
  }
</style>
</head>
<body>
  <main class="cover">
    <p class="cover__author">BERNARD MORLAIX</p>

    <div class="cover__illustration" role="img"
         aria-label="Colourful burst of school items: apple, pencils, paint palette, open book, test tubes, scissors, laptop, footballs, ruler and floating letters and numbers"></div>

    <svg class="cover__arc" viewBox="0 0 820 80" aria-hidden="true">
      <defs>
        <linearGradient id="arcShade" x1="0" y1="0" x2="1" y2="0">
          <stop offset="0" stop-color="var(--arc-shade)"/>
          <stop offset="0.5" stop-color="var(--arc-light)"/>
          <stop offset="1" stop-color="var(--arc-shade)"/>
        </linearGradient>
      </defs>
      <path d="M0 70 Q410 -20 820 72 L820 80 Q410 8 0 80 Z" fill="url(#arcShade)"/>
      <path d="M0 80 Q410 8 820 80 L820 80 L0 80 Z" fill="var(--paper)"/>
    </svg>

    <h1 class="cover__title">
      <span class="cover__title-main">The Lively Pen</span>
      <span class="cover__title-echo">lively pen!</span>
    </h1>

    <p class="cover__publisher">Quillon Editions</p>
  </main>
</body>
</html>
```